Rimah Advertising & Publicity business cards

I would like my Company's business card to be designed creatively & profissionally the logo is attached in both Arabic & english and prefer to have my emblem dimmed on the card as well
-Logo ( Arabic & English)
-Name (Arabic & English)
-Title ( Arabic & English)
-----------
-Location
-Landline (icon)
-Mobile phone (icon)
-Email (icon)
-Instagram (icon)
-WhatsApp (icon)

Target Market(s)

Industry/Entity Type

Marketing

Contact Information for Business Card

-Logo ( Arabic & English)
-Name (Arabic & English)
-----------
-Location
-Landline (icon)
-Mobile phone (icon)
-Email (icon)
-Instagram (icon)
-WhatsApp (icon)

Font styles to use
Serif

Requirements
Must have
• all what is mentions in business card details blanked and i will add the data my self
Nice to have
• Dim emblem on my business card both Arabic & english

```html
<!DOCTYPE html>
<html lang="en">
<head>
<meta charset="utf-8">
<title>Rimah Advertising &amp; Publicity — Business Card</title>
<link rel="stylesheet" href="https://fonts.googleapis.com/css2?family=Questrial&family=Open+Sans:wght@400;600&display=swap">
<style>
  :root {
    --page-bg: #d8d4cd;
    --card-front: #060606;
    --card-back: #4fc4c6;
    --teal: #4fc9c9;
    --white: #f2f2f2;
    --grey: #b9b9b9;
    --ink: #1a1a1a;
  }
  * { box-sizing: border-box; margin: 0; padding: 0; }
  html, body {
    width: 1200px;
    height: 1000px;
    overflow: hidden;
    background: var(--page-bg);
  }
  .business-card {
    position: absolute;
    left: 220px;
    width: 760px;
    height: 434px;
    border-radius: 6px;
    box-shadow: 0 14px 34px rgba(0,0,0,0.3);
    overflow: hidden;
  }
  .card-front { top: 46px; background: var(--card-front); }
  .card-back { top: 520px; background: var(--card-back); }

  /* Front */
  .emblem-mark {
    position: absolute;
    left: 70px;
    top: 185px;
    width: 100px;
    height: 100px;
    background: var(--teal);
    border-radius: 4px;
  }
  .brand-divider {
    position: absolute;
    left: 205px;
    top: 90px;
    width: 2px;
    height: 150px;
    background: var(--teal);
  }
  .brand-name {
    position: absolute;
    left: 228px;
    top: 48px;
    font-family: "Questrial", sans-serif;
    font-size: 96px;
    line-height: 1;
    color: var(--teal);
    letter-spacing: 2px;
  }
  .brand-tagline {
    position: absolute;
    left: 232px;
    top: 156px;
    font-family: "Questrial", sans-serif;
    font-size: 30px;
    line-height: 1.2;
    color: var(--white);
    letter-spacing: 1px;
  }
  .contact-list {
    position: absolute;
    left: 440px;
    top: 218px;
    list-style: none;
  }
  .contact-item {
    display: flex;
    align-items: center;
    gap: 12px;
    height: 29px;
    font-family: "Open Sans", sans-serif;
    font-size: 16px;
    color: var(--teal);
    white-space: nowrap;
  }
  .contact-icon { width: 18px; height: 18px; flex: none; }
  .person {
    position: absolute;
    left: 230px;
    top: 322px;
    width: 180px;
    text-align: center;
  }
  .person-name {
    font-family: "Open Sans", sans-serif;
    font-size: 28px;
    color: var(--teal);
    line-height: 1.1;
    white-space: nowrap;
  }
  .person-title {
    font-family: "Open Sans", sans-serif;
    font-size: 12px;
    color: var(--grey);
    letter-spacing: 1px;
    margin-top: 4px;
  }

  /* Back */
  .back-lockup {
    position: absolute;
    inset: 0;
    display: flex;
    flex-direction: column;
    align-items: center;
    justify-content: center;
  }
  .back-name {
    font-family: "Questrial", sans-serif;
    font-size: 190px;
    line-height: 1;
    color: var(--white);
    letter-spacing: 4px;
  }
  .back-tagline {
    font-family: "Questrial", sans-serif;
    font-size: 38px;
    line-height: 1.2;
    color: var(--ink);
    margin-top: 10px;
    letter-spacing: 1px;
  }
</style>
</head>
<body>
  <article class="business-card card-front">
    <div class="emblem-mark" role="img" aria-label="Company emblem"></div>
    <div class="brand-divider"></div>
    <div class="brand-name">Rimah</div>
    <div class="brand-tagline">Advertising &amp; Publicity</div>

    <ul class="contact-list">
      <li class="contact-item">
        <svg class="contact-icon" viewBox="0 0 22 22"><circle cx="11" cy="11" r="9" fill="none" stroke="#f2f2f2" stroke-width="2"/><path d="M8 7 L10 9 L9 10 Q11 13 13 13 L14 12 L16 14 L14 16 Q8 15 6 9 Z" fill="#f2f2f2"/></svg>
        <span>+966 555 0142</span>
      </li>
      <li class="contact-item">
        <svg class="contact-icon" viewBox="0 0 22 22"><rect x="2" y="2" width="18" height="18" rx="3" fill="none" stroke="#f2f2f2" stroke-width="2"/><circle cx="11" cy="11" r="4" fill="none" stroke="#f2f2f2" stroke-width="2"/></svg>
        <span>rimah.studio</span>
      </li>
      <li class="contact-item">
        <svg class="contact-icon" viewBox="0 0 22 22"><rect x="6" y="1" width="10" height="20" rx="2" fill="none" stroke="#f2f2f2" stroke-width="2"/><circle cx="11" cy="17" r="1.3" fill="#f2f2f2"/></svg>
        <span>+966 555 0187</span>
      </li>
      <li class="contact-item">
        <svg class="contact-icon" viewBox="0 0 22 22"><path d="M3 8 Q11 2 19 8 L17 11 L14 9 L8 9 L5 11 Z" fill="#f2f2f2"/><rect x="4" y="12" width="14" height="8" rx="1" fill="#f2f2f2"/></svg>
        <span>+966 11 555 0123</span>
      </li>
      <li class="contact-item">
        <svg class="contact-icon" viewBox="0 0 22 22"><rect x="2" y="4" width="18" height="14" fill="none" stroke="#f2f2f2" stroke-width="2"/><path d="M2 5 L11 12 L20 5" fill="none" stroke="#f2f2f2" stroke-width="2"/></svg>
        <span>hello@rimahstudio.com</span>
      </li>
      <li class="contact-item">
        <svg class="contact-icon" viewBox="0 0 22 22"><path d="M11 21 C5 13 4 11 4 8 A7 7 0 0 1 18 8 C18 11 17 13 11 21 Z" fill="#f2f2f2"/><circle cx="11" cy="8" r="2.5" fill="#060606"/></svg>
        <span>12 Palm Road, Suite 4</span>
      </li>
    </ul>

    <div class="person">
      <div class="person-name">Sami Haddad</div>
      <div class="person-title">OWNER</div>
    </div>
  </article>

  <article class="business-card card-back">
    <div class="back-lockup">
      <div class="back-name">Rimah</div>
      <div class="back-tagline">Advertising &amp; Publicity</div>
    </div>
  </article>
</body>
</html>
```